Wordpress Website Design - Scroll Style

Digital marketing agency needs a website redesign and installation of design. Website is built on Wordpress so the designer should keep Wordpress in mind. We have included images, Homepage copy, Customer Experience page copy, What We Do page copy, documents and a read me file to help guide the design.

Target Market(s)

Franchise owners and Local business owners with 10+ locations.

Industry/Entity Type

Marketing

Coding

Coded - Design and coding required

Number of Pages Required

3 page

Font styles to use
Sans Serif

Requirements
Must have
• Must incorporate the website copy and other images and files uploaded. Must resize for mobile friendly use with easy to read font and font size. Scroll style website. Editable text rather than text embedded in an image.
Nice to have
• na
Should not have
• na

```html
<!DOCTYPE html>
<html lang="en">
<head>
<meta charset="utf-8">
<title>Summit Reach Marketing</title>
<link href="https://fonts.googleapis.com/css2?family=Open+Sans:wght@400;600;700&family=Cinzel:wght@400;700&display=swap" rel="stylesheet">
<style>
:root{
  --blue:#1f7fc4;
  --blue-dark:#166aa6;
  --ink:#2b2b2b;
  --muted:#6d6d6d;
  --line:#dcdcdc;
  --grey-bg:#f1f1f1;
  --dark:#2a2c2f;
  --darker:#222427;
  --white:#ffffff;
}
*{box-sizing:border-box;margin:0;padding:0}
html,body{width:1200px;height:3600px;overflow:hidden}
body{font-family:"Open Sans",Arial,sans-serif;color:var(--ink);background:var(--white);position:relative}
section,header,footer{position:absolute;left:0;width:1200px}
.serif{font-family:"Cinzel",Georgia,serif}

/* header */
.site-header{top:0;height:80px;background:var(--white);display:flex;align-items:center;justify-content:space-between;padding:0 70px;border-bottom:1px solid var(--line)}
.brand{display:flex;align-items:center;gap:10px;font-weight:700;font-size:17px;color:var(--blue)}
.brand-dot{width:26px;height:26px;border-radius:50%;background:var(--blue)}
.main-nav{display:flex;gap:34px;font-size:14px;color:var(--ink)}
.main-nav .active{color:var(--blue);border-bottom:2px solid var(--blue);padding-bottom:4px}

/* hero */
.hero{top:80px;height:540px;background:linear-gradient(180deg,#3b4046 0%,#24272b 100%)}
.hero-headline{position:absolute;left:270px;top:50px;width:660px;background:rgba(0,0,0,.45);color:var(--white);text-align:center;padding:26px 20px}
.hero-headline h1{font-size:28px;font-weight:700;line-height:1.3}
.hero-headline p{font-size:16px;margin-top:14px}
.hero-features{position:absolute;left:0;right:0;top:250px;display:flex;justify-content:center;gap:70px}
.feature{width:130px;text-align:center;color:var(--white);font-size:13px}
.feature-icon{width:100px;height:100px;border-radius:50%;background:var(--white);margin:0 auto 14px;display:flex;align-items:center;justify-content:center}
.feature-icon.is-active{background:var(--blue)}
.slider-dots{position:absolute;top:470px;left:0;right:0;display:flex;justify-content:center;gap:12px}
.slider-dots span{width:12px;height:12px;border-radius:50%;border:2px solid var(--white)}
.slider-dots span.on{background:var(--white)}

/* intro */
.intro{top:620px;height:340px;text-align:center;padding-top:40px}
.intro-title{font-size:34px;color:var(--blue);font-weight:700}
.intro-sub{font-size:15px;color:var(--muted);margin-top:6px}
.intro-copy{width:900px;margin:24px auto 0;font-size:13px;line-height:1.75;color:var(--muted)}
.intro-copy p+p{margin-top:12px}
.btn-row{display:flex;justify-content:center;gap:10px;margin-top:22px}
.btn{display:inline-block;padding:9px 18px;font-size:13px;color:var(--white);background:var(--blue)}
.btn.dark{background:var(--dark)}

/* what we do */
.what-we-do{top:960px;height:600px;background:var(--grey-bg);text-align:center;padding-top:44px}
.section-title{font-size:32px;letter-spacing:2px;color:var(--ink)}
.section-sub{font-size:15px;color:var(--muted);margin-top:6px}
.wwd-hub{position:absolute;left:470px;top:170px;width:260px;height:260px;border-radius:50%;border:18px solid var(--blue);background:var(--white);display:flex;align-items:center;justify-content:center;flex-direction:column;font-weight:700;color:var(--blue);font-size:16px;gap:8px}
.wwd-hub .mark{width:36px;height:36px;border-radius:50%;background:var(--blue)}
.wwd-item{position:absolute;width:300px;font-size:12px;line-height:1.6;color:var(--muted)}
.wwd-item h3{font-size:16px;color:var(--ink);font-weight:600;margin-bottom:4px}
.wwd-item .pin{position:absolute;top:0;width:30px;height:30px;border-radius:50%;background:var(--blue)}
.wwd-item.left{text-align:right}
.wwd-item.left .pin{right:-44px}
.wwd-item.right{text-align:left}
.wwd-item.right .pin{left:-44px}
.wwd-item.bottom{text-align:center}

/* counters */
.counters{top:1560px;height:340px;text-align:center;padding-top:40px}
.counters h2{font-size:24px;font-weight:600}
.counter-row{position:absolute;left:90px;top:130px;display:flex;gap:50px}
.counter{width:130px;text-align:center}
.counter-ring{width:120px;height:120px;border-radius:50%;border:6px solid var(--dark);display:flex;align-items:center;justify-content:center;font-size:24px;font-weight:700;margin:0 auto}
.counter p{font-size:13px;color:var(--muted);margin-top:10px}
.phone-visual{position:absolute;left:860px;top:30px;width:230px;height:300px;border-radius:20px;background:linear-gradient(160deg,#d8dde2,#7e8a95)}

/* blue band */
.dashboard-band{top:1900px;height:400px;background:var(--blue);color:var(--white)}
.dashboard-visual{position:absolute;left:90px;top:50px;width:460px;height:300px;background:linear-gradient(160deg,#eef2f5,#b9c6d2);border-radius:6px}
.band-copy{position:absolute;left:640px;top:60px;width:470px}
.band-copy h3{font-size:20px;font-weight:700}
.band-copy p{font-size:14px;margin:6px 0 22px;line-height:1.6}
.btn.light{background:var(--white);color:var(--blue);font-weight:700}

/* clients */
.clients{top:2300px;height:260px;text-align:center;padding-top:40px}
.client-row{display:flex;justify-content:center;gap:30px;margin-top:40px}
.client{width:170px;height:90px;border:1px solid var(--line);display:flex;align-items:center;justify-content:center;gap:8px;font-size:14px;font-weight:600;color:var(--muted)}
.client .sq{width:16px;height:16px;background:var(--muted)}

/* reviews */
.reviews{top:2560px;height:420px;background:var(--grey-bg);text-align:center;padding-top:40px}
.review-row{display:flex;justify-content:center;gap:30px;margin-top:40px}
.review{width:330px;background:var(--white);border:1px solid var(--line);padding:22px;text-align:left;font-size:13px;line-height:1.6;color:var(--muted)}
.review-head{display:flex;gap:10px;align-items:center;margin-bottom:12px}
.review-head .sq{width:34px;height:34px;background:var(--blue)}
.review-head b{display:block;color:var(--ink);font-size:14px}
.review time{display:block;margin-top:12px;font-size:12px}

/* contact */
.contact{top:2980px;height:560px;background:var(--dark);color:var(--white);padding:50px 90px}
.contact h2{font-size:24px;font-weight:400}
.contact h2 span{color:var(--blue)}
.contact-form{position:absolute;left:90px;top:120px;width:560px;display:grid;grid-template-columns:1fr 1fr;gap:16px}
.field{height:44px;border:1px solid #555;background:#33363a;font-size:13px;color:#aaa;padding:12px}
.field.wide{grid-column:1/3;height:150px}
.btn.send{grid-column:1/2;width:200px;padding:12px 18px}
.contact-info{position:absolute;left:760px;top:130px;width:360px}
.info-line{display:flex;align-items:center;gap:16px;font-size:14px;margin-bottom:40px;line-height:1.5}
.info-line .ic{flex:none;width:46px;height:46px;border-radius:50%;background:var(--white);display:flex;align-items:center;justify-content:center}
.bottom-bar{top:3540px;height:60px;background:var(--blue);color:var(--white);display:flex;align-items:center;justify-content:space-between;padding:0 90px;font-size:13px}
.social{display:flex;gap:10px}
.social span{width:28px;height:28px;border-radius:50%;border:2px solid var(--white)}
</style>
</head>
<body>

<header class="site-header">
  <div class="brand"><span class="brand-dot"></span>Summit Reach Marketing</div>
  <nav class="main-nav">
    <span class="active">what we do</span><span>Attract Customers</span><span>Grow Revenue</span><span>Reduce Costs</span><span>Blog</span><span>Contact Us</span>
  </nav>
</header>

<section class="hero" role="img" aria-label="Dark photo of a marketing team at work behind the headline">
  <div class="hero-headline">
    <h1>Overwhelmed by your online marketing efforts and underwhelmed by results?</h1>
    <p>We track and manage every online marketing action</p>
  </div>
  <div class="hero-features">
    <div class="feature"><div class="feature-icon"><svg width="50" height="50" viewBox="0 0 50 50" fill="none" stroke="#1f7fc4" stroke-width="3"><circle cx="25" cy="25" r="20"/><circle cx="25" cy="25" r="11"/><circle cx="25" cy="25" r="3" fill="#1f7fc4"/></svg></div>Results Driven</div>
    <div class="feature"><div class="feature-icon is-active"><svg width="50" height="50" viewBox="0 0 50 50" fill="none" stroke="#fff" stroke-width="3"><circle cx="25" cy="25" r="20"/><path d="M25 13v12l8 6"/></svg></div>Minimal Time Commitment</div>
    <div class="feature"><div class="feature-icon"><svg width="50" height="50" viewBox="0 0 50 50" fill="none" stroke="#1f7fc4" stroke-width="4"><path d="M12 26l9 9 17-19"/></svg></div>Affordable</div>
    <div class="feature"><div class="feature-icon"><svg width="50" height="50" viewBox="0 0 50 50" fill="#1f7fc4"><rect x="10" y="28" width="7" height="14"/><rect x="21" y="18" width="7" height="24"/><rect x="32" y="10" width="7" height="32"/></svg></div>Clear Reporting</div>
  </div>
  <div class="slider-dots"><span class="on"></span><span></span><span></span></div>
</section>

<section class="intro">
  <div class="intro-title">Summit Reach Marketing</div>
  <div class="intro-sub">Results-Driven Digital Marketing for Your Local Business</div>
  <div class="intro-copy">
    <p>Digital marketing is critical for your local business. Most consumers now turn to search before they visit a store, call a shop or book a service. Yet making your way through listings, reviews, social posts, paid ads and coupons can feel endless. Every channel promises growth, but few show you what is truly working, which calls came in, and where your budget actually goes each month across every single location.</p>
    <p>Summit Reach is a digital marketing platform and service provider focused on managing and controlling the online presence of franchises and local businesses from one easy-to-use interface.</p>
  </div>
  <div class="btn-row"><span class="btn">Read More</span><span class="btn dark">Contact Us</span></div>
</section>

<section class="what-we-do">
  <h2 class="section-title serif">What We Do</h2>
  <div class="section-sub">Results-Driven Digital Marketing for Your Local Business</div>
  <div class="wwd-hub"><span class="mark"></span>Summit Reach<br>Marketing</div>
  <div class="wwd-item left" style="left:120px;top:180px"><span class="pin"></span><h3>Reduce Costs</h3>Cut costs by automating many daily management tasks and identifying where ad spend is not paying off.</div>
  <div class="wwd-item left" style="left:120px;top:320px"><span class="pin"></span><h3>Delight Clients</h3>Make it easy for customers to reach you and respond to feedback on every channel.</div>
  <div class="wwd-item right" style="left:780px;top:180px"><span class="pin"></span><h3>Attract Customers</h3>Attract new customers through targeted ads, optimized listings and steady reputation management.</div>
  <div class="wwd-item right" style="left:780px;top:320px"><span class="pin"></span><h3>Grow Revenue</h3>Grow the lifetime value of your customers with automated nurture and retention campaigns.</div>
  <div class="wwd-item bottom" style="left:450px;top:460px"><h3>Visualize Measure</h3>See the real value of each campaign through email, SMS, voice and direct mail reports.</div>
</section>

<section class="counters">
  <h2>Counter Ratings</h2>
  <div class="counter-row">
    <div class="counter"><div class="counter-ring">248</div><p>Satisfied Clients</p></div>
    <div class="counter"><div class="counter-ring">89500</div><p>Coupons Received</p></div>
    <div class="counter"><div class="counter-ring">266688</div><p>Calls Generated</p></div>
    <div class="counter"><div class="counter-ring">118385</div><p>Social Posts</p></div>
  </div>
  <div class="phone-visual" role="img" aria-label="Hand holding a smartphone showing the reporting app"></div>
</section>

<section class="dashboard-band">
  <div class="dashboard-visual" role="img" aria-label="Desktop monitor showing a revenue dashboard with charts and figures"></div>
  <div class="band-copy">
    <h3>ROI:</h3><p>Identify the total revenue generated by your campaign spend.</p>
    <h3>Digital Leads:</h3><p>View the leads SRM has generated for your business and identify the campaign source.</p>
    <h3>Manage Reviews:</h3><p>Obtain reviews and see all of them in one place.</p>
    <span class="btn light">SCHEDULE A DEMO</span>
  </div>
</section>

<section class="clients">
  <h2 class="section-title serif">Client Logos</h2>
  <div class="client-row">
    <div class="client"><span class="sq"></span>COMPANY</div>
    <div class="client"><span class="sq"></span>COMPANY</div>
    <div class="client"><span class="sq"></span>COMPANY</div>
    <div class="client"><span class="sq"></span>COMPANY</div>
    <div class="client"><span class="sq"></span>COMPANY</div>
  </div>
</section>

<section class="reviews">
  <h2 class="section-title serif">Customer Reviews</h2>
  <div class="review-row">
    <div class="review"><div class="review-head"><span class="sq"></span><div><b>Brightline</b>@brightline</div></div>Great working with the team on our local listings. Calls from new customers climbed in the first month and the weekly reports are clear and easy to follow.<time>7:29 AM - 6 Jan 2016</time></div>
    <div class="review"><div class="review-head"><span class="sq"></span><div><b>Brightline</b>@brightline</div></div>Managing reviews for all of our stores used to take hours. Now it lives in one place and our ratings have improved across every single location we run.<time>7:29 AM - 6 Jan 2016</time></div>
    <div class="review"><div class="review-head"><span class="sq"></span><div><b>Brightline</b>@brightline</div></div>We finally know which campaigns bring in revenue. The dashboard shows leads by source, so cutting wasted spend was easy and fast for our whole franchise group.<time>7:29 AM - 6 Jan 2016</time></div>
  </div>
</section>

<section class="contact">
  <h2>Questions, Comments? <span>Let us know!</span></h2>
  <div class="contact-form">
    <div class="field">First Name</div><div class="field">Last Name</div>
    <div class="field">Phone Number</div><div class="field">E-Mail Address</div>
    <div class="field wide">Message</div>
    <span class="btn send">Send Your Message</span>
  </div>
  <div class="contact-info">
    <div class="info-line"><span class="ic"><svg width="22" height="22" viewBox="0 0 22 22" fill="none" stroke="#2a2c2f" stroke-width="2"><rect x="2" y="5" width="18" height="12"/><path d="M2 5l9 7 9-7"/></svg></span>Email: hello@summitreach.com</div>
    <div class="info-line"><span class="ic"><svg width="22" height="22" viewBox="0 0 22 22" fill="#2a2c2f"><path d="M11 1a7 7 0 0 0-7 7c0 5 7 13 7 13s7-8 7-13a7 7 0 0 0-7-7zm0 10a3 3 0 1 1 0-6 3 3 0 0 1 0 6z"/></svg></span>Riverside - 210 Harbor Street, Lakeview City</div>
    <div class="info-line"><span class="ic"><svg width="22" height="22" viewBox="0 0 22 22" fill="#2a2c2f"><path d="M5 2l4 4-2 3c1 3 3 5 6 6l3-2 4 4-3 3C9 20 2 13 2 5z"/></svg></span>Phone: (555) 014-2290</div>
  </div>
</section>

<footer class="bottom-bar">
  <span>Copyright © 2016 · SummitReach · All rights reserved.</span>
  <div class="social"><span></span><span></span><span></span><span></span></div>
</footer>

</body>
</html>
```